New website for Varnipo.se - self employment agency for freelance workers

[NOTE THE CODED ADD-ON HAS BEEN INCLUDED ALREADY (DC ADMIN)] New layout based on Wordpress themes including migration of existing content at varnipo.se. Want to use existing logotype as guideline for total layout concept. Please use existing structure and text content on varnipo.se. Existing pictures are optional to reuse. The secured part of the existing website under "Logga in" is not part of this project.

Target Market(s)

Self employment within all industries and ages above 16.

Industry/Entity Type

Finance And Accounting

Font styles to use
Other font styles liked:
• Should match with logotype

Colors
3176b5
85abd2
cfdeed

Requirements
Must have
• Ready to use wordpress themes. Include salary calculation bar as in existing website. Multi lingual ready(today only in Swedish). Mobile client responsive.

```html
<!DOCTYPE html>
<html lang="sv">
<head>
<meta charset="utf-8">
<title>Varnipo.se – Startsida</title>
<link href="https://fonts.googleapis.com/css2?family=Raleway:wght@300;400&family=Arimo:wght@400&display=swap" rel="stylesheet">
<style>
  :root {
    --brand-blue: #3176b5;
    --brand-mid: #85abd2;
    --brand-pale: #cfdeed;
    --hero-light: #1f9be0;
    --hero-deep: #2a2f8f;
    --ink: #1a1a1a;
    --nav-dark: #1c1c1c;
    --white: #ffffff;
  }
  * { box-sizing: border-box; margin: 0; padding: 0; }
  html, body { width: 1200px; height: 953px; overflow: hidden; background: var(--white); }
  .page { position: relative; width: 1200px; height: 953px; overflow: hidden; font-family: "Arimo", Arial, sans-serif; color: var(--ink); }

  .site-header { position: absolute; top: 0; left: 0; width: 1200px; height: 62px; background: var(--white); border-top: 3px solid var(--brand-blue); z-index: 3; }
  .nav-link { position: absolute; top: 24px; font-size: 12px; color: #333; text-decoration: none; }
  .nav-link--active { top: 0; height: 59px; left: 216px; width: 64px; background: var(--nav-dark); color: var(--white); display: flex; align-items: center; justify-content: center; }
  .nav-jobba { left: 330px; }
  .nav-foretag { left: 770px; }
  .nav-om { left: 862px; }
  .nav-logga { left: 952px; }

  .logo-tab { position: absolute; top: 0; left: 480px; width: 240px; height: 172px; z-index: 4; }
  .logo { position: absolute; top: 90px; left: 480px; width: 240px; display: flex; align-items: center; justify-content: center; gap: 8px; z-index: 5; }
  .logo-mark { width: 10px; height: 10px; background: var(--brand-blue); }
  .logo-name { font-family: "Raleway", sans-serif; font-weight: 400; font-size: 24px; letter-spacing: 3px; color: var(--ink); }

  .hero { position: absolute; top: 62px; left: 0; width: 1200px; height: 560px; background: linear-gradient(100deg, var(--hero-light) 0%, var(--brand-blue) 45%, var(--hero-deep) 100%); }
  .hero-fade { position: absolute; top: 622px; left: 0; width: 1200px; height: 100px; background: linear-gradient(180deg, var(--brand-blue) 0%, var(--brand-mid) 45%, var(--brand-pale) 75%, var(--white) 100%); }
  .hero-title { position: absolute; top: 345px; left: 0; width: 1200px; text-align: center; font-family: "Raleway", sans-serif; font-weight: 300; font-size: 44px; letter-spacing: 1px; color: var(--white); z-index: 2; }
  .hero-button { position: absolute; top: 430px; left: 470px; width: 260px; height: 46px; border: 1px solid var(--white); border-radius: 23px; color: var(--white); font-family: "Raleway", sans-serif; font-size: 16px; letter-spacing: 2px; display: flex; align-items: center; justify-content: center; text-decoration: none; z-index: 2; }

  .intro { position: absolute; top: 762px; left: 0; width: 1200px; text-align: center; font-size: 27px; line-height: 1.3; color: var(--ink); }
  .divider { position: absolute; top: 862px; left: 560px; width: 80px; height: 2px; background: var(--brand-blue); }
</style>
</head>
<body>
<div class="page">
  <header class="site-header">
    <nav>
      <a class="nav-link nav-link--active" href="#">HEM</a>
      <a class="nav-link nav-jobba" href="#">Jobba som egenanställd</a>
      <a class="nav-link nav-foretag" href="#">Företag</a>
      <a class="nav-link nav-om" href="#">Om oss</a>
      <a class="nav-link nav-logga" href="#">Logga in</a>
    </nav>
  </header>

  <svg class="logo-tab" viewBox="0 0 240 172" aria-hidden="true">
    <polygon points="0,0 240,0 240,140 120,172 0,140" fill="#ffffff"/>
  </svg>
  <div class="logo">
    <span class="logo-mark"></span>
    <span class="logo-name">VARNIPO</span>
  </div>

  <section class="hero" role="img" aria-label="Foto: person med utsträckta armar framför en stadssiluett, tonat i blått"></section>
  <div class="hero-fade" role="img" aria-label="Övergång från blått till vitt"></div>
  <h1 class="hero-title">WORK ON YOUR OWN TERMS</h1>
  <a class="hero-button" href="#">BLI EGENANSTÄLLD</a>

  <p class="intro">Fakturera utan eget företag,<br>anlita medarbetare utan att anställa</p>

  <div class="divider" aria-hidden="true"></div>
</div>
</body>
</html>
```